Veltarum

Standard Business Card design.
Sample two-sided design uploaded. White front, Black back.
Would like white shield to be on all black background side.
Willing to look at a couple creative designs, but nothing crazy.
Preference for a classic, confident, strong design.

```html
<!DOCTYPE html>
<html lang="en">
<head>
<meta charset="utf-8">
<title>Veltarum Business Card</title>
<link rel="stylesheet" href="https://fonts.googleapis.com/css2?family=Poppins:wght@400;600&display=swap">
<style>
  :root {
    --backdrop: #e4e4e4;
    --ink: #000000;
    --paper: #ffffff;
    --text: #1a1a1a;
    --card-radius: 54px;
  }
  * { margin: 0; padding: 0; box-sizing: border-box; }
  html, body {
    width: 1200px;
    height: 900px;
    overflow: hidden;
    background: var(--backdrop);
    font-family: "Poppins", sans-serif;
  }
  .stage { position: relative; width: 1200px; height: 900px; }
  .card {
    position: absolute;
    top: 217px;
    width: 309px;
    height: 500px;
    box-shadow: 2px 3px 6px rgba(0,0,0,0.35);
  }
  .card-back {
    left: 279px;
    background: var(--ink);
    border-radius: 0 var(--card-radius) 0 var(--card-radius);
  }
  .card-front {
    left: 617px;
    background: var(--paper);
    border-radius: var(--card-radius) 0 var(--card-radius) 0;
    color: var(--text);
  }
  .back-name {
    position: absolute;
    left: 0; right: 0;
    top: 228px;
    text-align: center;
    color: var(--paper);
    font-weight: 600;
    font-size: 34px;
    letter-spacing: 3px;
    text-transform: uppercase;
  }
  .front-name {
    position: absolute;
    left: 0; right: 0;
    top: 180px;
    text-align: center;
    color: var(--ink);
    font-weight: 600;
    font-size: 32px;
    letter-spacing: 3px;
    text-transform: uppercase;
  }
  .holder {
    position: absolute;
    left: 32px;
    top: 306px;
  }
  .holder-name {
    font-weight: 600;
    font-size: 19px;
    line-height: 22px;
    color: var(--ink);
  }
  .holder-title {
    font-size: 13.5px;
    line-height: 17px;
  }
  .contact-list {
    position: absolute;
    left: 32px;
    top: 359px;
    list-style: none;
    font-size: 13.5px;
    line-height: 18px;
  }
  .contact-list li { display: flex; align-items: center; gap: 5px; }
  .contact-list svg { width: 12px; height: 12px; flex: none; }
  .address {
    position: absolute;
    left: 33px;
    top: 427px;
    font-size: 13.5px;
    line-height: 18px;
    font-style: normal;
  }
</style>
</head>
<body>
<main class="stage">
  <section class="card card-back">
    <p class="back-name">Veltarum</p>
  </section>

  <section class="card card-front">
    <p class="front-name">Veltarum</p>

    <div class="holder">
      <p class="holder-name">DANIEL HARWICK</p>
      <p class="holder-title">Managing Director</p>
    </div>

    <ul class="contact-list">
      <li>
        <svg viewBox="0 0 24 24" aria-hidden="true"><path fill="none" stroke="#1a1a1a" stroke-width="2.4" d="M5 3h4l2 5-2.5 1.5a11 11 0 0 0 6 6L16 13l5 2v4a2 2 0 0 1-2 2A16 16 0 0 1 3 5a2 2 0 0 1 2-2z"/></svg>
        044-555 210 347
      </li>
      <li>
        <svg viewBox="0 0 24 24" aria-hidden="true"><rect x="2" y="5" width="20" height="14" fill="#1a1a1a"/><path d="M2 5l10 8 10-8" fill="none" stroke="#fff" stroke-width="2"/></svg>
        info@veltarum.com
      </li>
      <li>
        <svg viewBox="0 0 24 24" aria-hidden="true"><g fill="none" stroke="#1a1a1a" stroke-width="2"><circle cx="12" cy="12" r="9.5"/><ellipse cx="12" cy="12" rx="4" ry="9.5"/><path d="M2.5 12h19M4 7h16M4 17h16"/></g></svg>
        www.veltarum.com
      </li>
    </ul>

    <address class="address">
      78, Harbour Lane, Eastgate<br>
      30917, Northland
    </address>
  </section>
</main>
</body>
</html>
```